Window Decal Design

I have office windows that need a design incorporating from my logo. It should be semi transparent and offer enough privacy for meetings.

Size of the window is 450cm by 295cm

Colors
F0912C
F2A743
F7CA91
FBE8D2
FDF5EE

```html
<!DOCTYPE html>
<html lang="en">
<head>
<meta charset="utf-8">
<title>Norvale Window Decal</title>
<link href="https://fonts.googleapis.com/css2?family=Montserrat:wght@700&display=swap" rel="stylesheet">
<style>
  :root {
    --wall: #eef0f1;
    --glass: #d3dde2;
    --frost: rgba(255, 255, 255, 0.62);
    --frost-bright: rgba(255, 255, 255, 0.55);
    --orange: #F0912C;
    --frame: #b9c0c4;
  }
  * { margin: 0; padding: 0; box-sizing: border-box; }
  html, body {
    width: 1200px;
    height: 900px;
    overflow: hidden;
    background: var(--wall);
  }
  .window-decal {
    position: absolute;
    left: 0;
    top: 56px;
    width: 1200px;
    height: 787px;
    background: var(--glass);
    outline: 6px solid var(--frame);
    outline-offset: -6px;
  }
  .decal-art { position: absolute; inset: 0; width: 100%; height: 100%; }
  .band-frost { fill: var(--frost); }
  .band-frost-bright { fill: var(--frost-bright); }
  .band-orange { fill: var(--orange); }
  .brand-name {
    position: absolute;
    left: 800px;
    top: 318px;
    width: 340px;
    display: flex;
    align-items: center;
    justify-content: center;
    gap: 18px;
    font-family: "Montserrat", sans-serif;
    font-weight: 700;
    font-size: 64px;
    letter-spacing: 1px;
    color: var(--orange);
  }
  .brand-dot {
    width: 30px;
    height: 30px;
    border-radius: 50%;
    background: var(--orange);
  }
</style>
</head>
<body>
  <main class="window-decal">
    <svg class="decal-art" viewBox="0 0 1200 787" aria-hidden="true">
      <rect class="band-frost" x="0" y="150" width="1200" height="16"/>
      <rect class="band-orange" x="0" y="178" width="1200" height="24"/>
      <rect class="band-frost" x="0" y="220" width="1200" height="28"/>
      <rect class="band-frost" x="0" y="262" width="1200" height="185"/>
      <polygon class="band-frost-bright" points="540,447 1200,262 1200,447"/>
      <rect class="band-frost" x="0" y="458" width="1200" height="36"/>
      <rect class="band-orange" x="0" y="510" width="1200" height="24"/>
      <rect class="band-frost" x="0" y="545" width="1200" height="10"/>
    </svg>
    <div class="brand-name"><span class="brand-dot"></span>Norvale</div>
  </main>
</body>
</html>
```